Stationary w/Bizz Card for Medical Equipment Company
Harborline Biomedical Systems
Stationary w/Bizz Card  for Medical Equipment Company - Health
Creative Brief
Professional
Derek Palmer
Vice President
415 Wexmoor Avenue Jacksonville, FL 32209
derek.palmer@hb-sysmed.net
www.hb-sysmed.net
Somewhere on the business card please put "Harborline Biomedical Systems"

```html
<!DOCTYPE html>
<html lang="en">
<head>
<meta charset="utf-8">
<title>Harborline Biomedical Systems – Business Card</title>
<link rel="stylesheet" href="https://fonts.googleapis.com/css2?family=Roboto:ital,wght@0,400;0,700;1,400&display=swap">
<style>
  :root {
    --stage: #e9e7e4;
    --card-white: #ffffff;
    --brand-blue: #1f9ad6;
    --brand-blue-deep: #0a6fb0;
    --brand-blue-light: #8fd0f0;
    --text-dark: #3a3a3a;
    --back-dark: #2f2f2f;
    --back-mid: #5c5c5c;
    --back-text: #ffffff;
  }
  * { box-sizing: border-box; margin: 0; padding: 0; }
  html, body { width: 1200px; height: 402px; overflow: hidden; }
  body {
    background: var(--stage);
    font-family: "Roboto", Arial, sans-serif;
    position: relative;
  }
  .card {
    position: absolute;
    top: 72px;
    width: 547px;
    height: 264px;
    overflow: hidden;
    box-shadow: 0 3px 10px rgba(0,0,0,0.25);
  }
  .card-front { left: 41px; background: var(--card-white); }
  .card-back {
    left: 617px;
    background: radial-gradient(ellipse at 50% 40%, var(--back-mid) 0%, var(--back-dark) 75%);
  }
  .front-wave { position: absolute; left: 0; bottom: 0; width: 547px; height: 110px; }
  .brand-mark {
    position: absolute;
    display: flex;
    align-items: center;
    gap: 10px;
    font-weight: 700;
  }
  .card-front .brand-mark { left: 48px; top: 72px; }
  .brand-dot {
    width: 20px; height: 20px; border-radius: 50%;
    background: var(--brand-blue);
  }
  .brand-name { font-size: 44px; color: var(--brand-blue); letter-spacing: 1px; }
  .person { position: absolute; left: 318px; top: 34px; }
  .person-name { font-size: 17px; font-weight: 700; color: var(--brand-blue); }
  .person-title { font-size: 12px; color: var(--text-dark); margin-top: 2px; }
  .contact-list {
    position: absolute; left: 318px; top: 88px;
    list-style: none;
  }
  .contact-item {
    display: flex; align-items: center; gap: 6px;
    font-size: 12px; color: var(--text-dark);
    height: 18px;
  }
  .contact-icon { width: 11px; height: 11px; flex: none; }
  .address {
    position: absolute; left: 28px; top: 212px;
    font-size: 12px; line-height: 16px; color: #ffffff;
  }
  .card-back .brand-mark {
    left: 0; right: 0; top: 72px; justify-content: center;
  }
  .card-back .brand-dot { background: var(--back-text); }
  .card-back .brand-name { color: var(--back-text); font-size: 58px; }
  .back-tagline {
    position: absolute; left: 0; right: 0; top: 168px;
    text-align: center; font-style: italic;
    font-size: 20px; color: var(--back-text);
  }
</style>
</head>
<body>
  <section class="card card-front">
    <svg class="front-wave" viewBox="0 0 547 110" preserveAspectRatio="none" aria-hidden="true">
      <path d="M0 40 C150 10 330 70 547 20 L547 110 L0 110 Z" fill="var(--brand-blue-light)"/>
      <path d="M0 52 C160 22 330 82 547 32 L547 110 L0 110 Z" fill="var(--brand-blue)"/>
      <path d="M0 80 C180 55 360 100 547 65 L547 110 L0 110 Z" fill="var(--brand-blue-deep)"/>
    </svg>
    <div class="brand-mark"><span class="brand-dot"></span><span class="brand-name">halvorn</span></div>
    <div class="person">
      <div class="person-name">Derek Palmer</div>
      <div class="person-title">Vice President</div>
    </div>
    <ul class="contact-list">
      <li class="contact-item"><svg class="contact-icon" viewBox="0 0 12 12"><circle cx="6" cy="6" r="6" fill="var(--brand-blue)"/><path d="M4 3 L5 5 L4.6 5.6 Q5.5 7 6.4 7.4 L7 7 L9 8 L8.5 9 Q5.5 9 3 5 Z" fill="#fff"/></svg>800-555-0142</li>
      <li class="contact-item"><svg class="contact-icon" viewBox="0 0 12 12"><circle cx="6" cy="6" r="6" fill="var(--brand-blue)"/><path d="M4 3 L5 5 L4.6 5.6 Q5.5 7 6.4 7.4 L7 7 L9 8 L8.5 9 Q5.5 9 3 5 Z" fill="#fff"/></svg>904-555-0187</li>
      <li class="contact-item"><svg class="contact-icon" viewBox="0 0 12 12"><circle cx="6" cy="6" r="6" fill="var(--brand-blue)"/><rect x="3.5" y="4" width="5" height="4" fill="#fff"/></svg>904-555-0163</li>
      <li class="contact-item"><svg class="contact-icon" viewBox="0 0 12 12"><circle cx="6" cy="6" r="6" fill="var(--brand-blue)"/><rect x="3" y="4" width="6" height="4" fill="#fff"/><path d="M3 4 L6 6.5 L9 4" stroke="var(--brand-blue)" stroke-width="0.7" fill="none"/></svg>derek.palmer@hb-sysmed.net</li>
      <li class="contact-item"><svg class="contact-icon" viewBox="0 0 12 12"><circle cx="6" cy="6" r="6" fill="var(--brand-blue)"/><circle cx="6" cy="6" r="3" fill="none" stroke="#fff" stroke-width="1"/></svg>www.hb-sysmed.net</li>
    </ul>
    <address class="address" style="font-style:normal">415 Wexmoor Avenue<br>Jacksonville, FL 32209</address>
  </section>

  <section class="card card-back">
    <div class="brand-mark"><span class="brand-dot"></span><span class="brand-name">halvorn</span></div>
    <p class="back-tagline">Harborline Biomedical Systems</p>
  </section>
</body>
</html>
```